Poster design for a company operating care homes in the UK showcasing our core values

We need a poster to display in our care homes showcasing our new core values:

Purpose
We are driven by a clear understanding of why we do what we do: to enrich lives, honour legacies and make a meaningful difference every day, for our residents, their families, our colleagues and our community.

Excellence
We hold ourselves to the highest standards, delivering exceptional care and creating an environment where both residents and staff can thrive.

Openness
We build trust through honest, respectful communication, welcoming feedback, sharing ideas, and embracing change as a path to continuous growth.

Passion
We are passionate about delivering exceptional care. We take pride in what we do and in making a real difference in people’s lives.

Learning
We are committed to personal and professional growth; empowering each other through ongoing development, reflection, and shared knowledge.

Empathy
We actively listen and seek to understand before being understood, recognising the unique stories, feelings, and needs of others.

I have attached a small graphic that we would like you try to incorporate, in addition to our company logo. Please theme the rest of the poster around our company colours.

```html
<!DOCTYPE html>
<html lang="en">
<head>
<meta charset="utf-8">
<title>Our Core Values – Harbourne</title>
<link rel="stylesheet" href="https://fonts.googleapis.com/css2?family=Archivo+Black&family=Inter:wght@400;500&family=Rubik+Dirt&display=swap">
<style>
  :root {
    --backdrop: #2C3442;
    --paper: #FCF4EE;
    --paper-deep: #F5E3D6;
    --navy: #3F4E6A;
    --navy-ink: #2F3D57;
    --tan: #DCA786;
    --frame: #DFDEE4;
    --white: #FFFFFF;
  }
  * { margin: 0; padding: 0; box-sizing: border-box; }
  html, body { width: 1200px; height: 1200px; overflow: hidden; background: var(--backdrop); }
  .poster {
    position: absolute; left: 235px; top: 87px;
    width: 1176px; height: 1652px;
    transform: scale(0.6211); transform-origin: 0 0;
    background: var(--paper); overflow: hidden;
    font-family: "Inter", Arial, sans-serif;
  }
  .poster-art { position: absolute; inset: 0; }
  .title {
    position: absolute; top: 12px; left: 0; width: 100%;
    text-align: center; font-family: "Archivo Black", "Arial Black", sans-serif;
    font-size: 78px; letter-spacing: 1px; color: var(--navy);
  }
  .title .accent { color: var(--tan); }
  .value { position: absolute; }
  .value h2 {
    display: block; white-space: nowrap;
    font-family: "Rubik Dirt", Impact, sans-serif; font-weight: 400;
    font-size: 36px; color: var(--tan); line-height: 36px;
    transform: scaleX(0.7);
  }
  .value p { margin-top: 14px; font-size: 21px; line-height: 24.6px; color: var(--navy-ink); }
  .value--left { left: 25px; text-align: left; }
  .value--left h2 { transform-origin: left center; }
  .value--right { right: 27px; text-align: right; }
  .value--right h2 { transform-origin: right center; }
  .brand {
    position: absolute; left: 0; width: 100%; top: 1495px; text-align: center;
    font-family: "Inter", Arial, sans-serif; font-weight: 500;
    font-size: 84px; letter-spacing: 1px; color: var(--navy-ink);
  }
</style>
</head>
<body>
<div class="poster">
  <svg class="poster-art" viewBox="0 0 1176 1652" width="1176" height="1652">
    <defs>
      <polygon id="word-hex" points="0,-100 86.6,-50 86.6,50 0,100 -86.6,50 -86.6,-50" stroke-linejoin="round" stroke-width="26"/>
      <polygon id="cell" points="0,-108 93.5,-54 93.5,54 0,108 -93.5,54 -93.5,-54"/>
      <polygon id="cell-frame" points="0,-128 110.9,-64 110.9,64 0,128 -110.9,64 -110.9,-64" stroke-linejoin="round"/>
    </defs>

    <polygon class="base-band" points="586,1297 1176,1652 0,1652" fill="var(--paper-deep)" stroke="var(--paper-deep)" stroke-width="30" stroke-linejoin="round"/>
    <line x1="460" y1="108" x2="704" y2="108" stroke="var(--navy)" stroke-width="3"/>

    <!-- PEOPLE word hexagons -->
    <g class="word-hexes" font-family="'Rubik Dirt', Impact, sans-serif">
      <g transform="translate(145 320) rotate(15)"><use href="#word-hex" fill="var(--tan)" stroke="var(--tan)"/></g>
      <g transform="translate(322 255) rotate(15)"><use href="#word-hex" fill="var(--navy)" stroke="var(--navy)"/></g>
      <g transform="translate(492 320) rotate(15)"><use href="#word-hex" fill="var(--tan)" stroke="var(--tan)"/></g>
      <g transform="translate(672 253) rotate(15)"><use href="#word-hex" fill="var(--navy)" stroke="var(--navy)"/></g>
      <g transform="translate(844 320) rotate(15)"><use href="#word-hex" fill="var(--tan)" stroke="var(--tan)"/></g>
      <g transform="translate(1022 253) rotate(15)"><use href="#word-hex" fill="var(--navy)" stroke="var(--navy)"/></g>

      <g class="word-label" fill="var(--navy)">
        <text x="87" y="351" font-size="72" textLength="43" lengthAdjust="spacingAndGlyphs">P</text>
        <text x="132" y="331" font-size="24" textLength="85" lengthAdjust="spacingAndGlyphs">URPOSE</text>
      </g>
      <g class="word-label" fill="var(--tan)">
        <text x="257" y="286" font-size="72" textLength="43" lengthAdjust="spacingAndGlyphs">E</text>
        <text x="303" y="262" font-size="22" textLength="94" lengthAdjust="spacingAndGlyphs">XCELLENCE</text>
      </g>
      <g class="word-label" fill="var(--navy)">
        <text x="430" y="351" font-size="72" textLength="42" lengthAdjust="spacingAndGlyphs">O</text>
        <text x="474" y="331" font-size="24" textLength="98" lengthAdjust="spacingAndGlyphs">PENNESS</text>
      </g>
      <g class="word-label" fill="var(--tan)">
        <text x="614" y="286" font-size="72" textLength="43" lengthAdjust="spacingAndGlyphs">P</text>
        <text x="660" y="263" font-size="24" textLength="77" lengthAdjust="spacingAndGlyphs">ASSION</text>
      </g>
      <g class="word-label" fill="var(--navy)">
        <text x="780" y="349" font-size="72" textLength="37" lengthAdjust="spacingAndGlyphs">L</text>
        <text x="819" y="328" font-size="24" textLength="94" lengthAdjust="spacingAndGlyphs">EARNING</text>
      </g>
      <g class="word-label" fill="var(--tan)">
        <text x="957" y="283" font-size="72" textLength="43" lengthAdjust="spacingAndGlyphs">E</text>
        <text x="1002" y="261" font-size="24" textLength="87" lengthAdjust="spacingAndGlyphs">MPATHY</text>
      </g>
    </g>

    <!-- connector lines -->
    <g class="connectors" fill="none" stroke="var(--navy)" stroke-width="3">
      <polyline points="25,497 265,497 427,603"/>
      <polyline points="1149,497 906,497 747,603"/>
      <polyline points="25,883 272,883"/>
      <polyline points="1149,883 902,883"/>
      <polyline points="25,1274 265,1274 427,1162"/>
      <polyline points="1149,1274 906,1274 747,1162"/>
    </g>

    <!-- honeycomb -->
    <g class="honeycomb">
      <g fill="var(--frame)" stroke="var(--navy)" stroke-width="6">
        <use href="#cell-frame" x="485" y="708"/><use href="#cell-frame" x="688" y="708"/>
        <use href="#cell-frame" x="385" y="885"/><use href="#cell-frame" x="586" y="885"/><use href="#cell-frame" x="788" y="885"/>
        <use href="#cell-frame" x="485" y="1063"/><use href="#cell-frame" x="688" y="1063"/>
      </g>
      <g fill="var(--frame)">
        <use href="#cell-frame" x="485" y="708"/><use href="#cell-frame" x="688" y="708"/>
        <use href="#cell-frame" x="385" y="885"/><use href="#cell-frame" x="586" y="885"/><use href="#cell-frame" x="788" y="885"/>
        <use href="#cell-frame" x="485" y="1063"/><use href="#cell-frame" x="688" y="1063"/>
      </g>
      <use href="#cell" x="485" y="708" fill="var(--tan)" role="img" aria-label="Purpose icon: target with arrow"/>
      <use href="#cell" x="688" y="708" fill="var(--navy)" role="img" aria-label="Passion icon: heart held in a hand"/>
      <use href="#cell" x="385" y="885" fill="var(--navy)" role="img" aria-label="Excellence icon: team with stars over a hand"/>
      <use href="#cell" x="788" y="885" fill="var(--tan)" role="img" aria-label="Learning icon: open book with light bulb"/>
      <use href="#cell" x="485" y="1063" fill="var(--tan)" role="img" aria-label="Openness icon: rising bar chart with arrow"/>
      <use href="#cell" x="688" y="1063" fill="var(--navy)" role="img" aria-label="Empathy icon: handshake forming a heart"/>
      <use href="#cell" x="586" y="885" fill="var(--white)" stroke="var(--navy)" stroke-width="4"/>
      <text x="586" y="894" text-anchor="middle" font-family="Inter, Arial, sans-serif" font-weight="500" font-size="28" fill="var(--navy-ink)">Harbourne</text>
      <g fill="var(--tan)" stroke="var(--navy)" stroke-width="3">
        <circle cx="427" cy="603" r="11"/><circle cx="747" cy="603" r="11"/>
        <circle cx="272" cy="883" r="11"/><circle cx="902" cy="883" r="11"/>
        <circle cx="427" cy="1162" r="11"/><circle cx="747" cy="1162" r="11"/>
      </g>
    </g>
  </svg>

  <h1 class="title"><span class="accent">OUR</span> CORE VALUES</h1>

  <section class="value value--left" style="top:459px; width:215px">
    <h2>PURPOSE</h2>
    <p>We are driven by a clear understanding of why we do what we do: to enrich lives, honour legacies and make a meaningful difference every day, for our residents, their families, our colleagues and our community.</p>
  </section>
  <section class="value value--right" style="top:459px; width:215px">
    <h2>PASSION</h2>
    <p>We are passionate about delivering exceptional care. We take pride in what we do and in making a real difference in people’s lives.</p>
  </section>
  <section class="value value--left" style="top:845px; width:210px">
    <h2>EXCELLENCE</h2>
    <p>We hold ourselves to the highest standards, delivering exceptional care and creating an environment where both residents and staff can thrive.</p>
  </section>
  <section class="value value--right" style="top:845px; width:210px">
    <h2>LEARNING</h2>
    <p>We are committed to personal and professional growth; empowering each other through ongoing development, reflection, and shared knowledge.</p>
  </section>
  <section class="value value--left" style="top:1236px; width:222px">
    <h2>OPENNESS</h2>
    <p>We build trust through honest, respectful communication, welcoming feedback, sharing ideas, and embracing change as a path to continuous growth.</p>
  </section>
  <section class="value value--right" style="top:1236px; width:215px">
    <h2>EMPATHY</h2>
    <p>We actively listen and seek to understand before being understood, recognising the unique stories, feelings, and needs of others.</p>
  </section>

  <div class="brand">HARBOURNE</div>
</div>
</body>
</html>
```